Romantic Experiences Business Needs Banner Ad Design Project

We are going to run a branding campaign and we need banner ad design for a company based in Mexico City called "CIRANDELLA".

We create romantic experiences or moments for couples celebrating special dates, for instance birthdays, wedding anniversaries and original ways to give an engagement ring. These experiences may have components like romantic dinner, chamber musicians, astronomer, concierges, fireworks, mansions, romantic tours on helicopter and yacht.

The final design should communicate our main task "romantic moment design" and brand attributes: sophisticated, elegant and romantic.

You can visit the webpage at: http://www.cirandella-example.com.mx

Target Market(s)

People from 25 to 50 years old who wants to celebrate wedding anniversary or give an engagement ring

Industry/Entity Type

Wedding

Requirements
Must have
• - Logo
- Banner sizes: 300x250, 728x90,160x600
Nice to have
• - Call to Action
- Theme: "Diseño Momentos Románticos"

```html
<!DOCTYPE html>
<html lang="es">
<head>
<meta charset="utf-8">
<title>CIRANDELLA — Momentos Románticos</title>
<link rel="stylesheet" href="https://fonts.googleapis.com/css2?family=Cinzel:wght@600&family=PT+Sans:wght@700&display=swap">
<style>
  :root {
    --stage: #b3b5b8;
    --navy-deep: #071a3a;
    --navy: #0e2c5c;
    --navy-glow: #1d4a85;
    --white: #ffffff;
    --button-top: #4cc6f5;
    --button-bottom: #1a9fe0;
    --button-edge: #0f7fc0;
  }
  * { margin: 0; padding: 0; box-sizing: border-box; }
  html, body {
    width: 1200px;
    height: 900px;
    overflow: hidden;
    background: var(--stage);
  }
  .banner {
    position: absolute;
    left: 375px;
    top: 262px;
    width: 450px;
    height: 375px;
    overflow: hidden;
    background:
      radial-gradient(ellipse 60% 55% at 38% 55%, var(--navy-glow) 0%, transparent 70%),
      linear-gradient(180deg, var(--navy-deep) 0%, var(--navy) 55%, var(--navy-deep) 100%);
  }
  .hero-photo {
    position: absolute;
    left: 215px;
    top: 78px;
    width: 235px;
    height: 297px;
    background:
      radial-gradient(ellipse 55% 40% at 62% 35%, rgba(214, 168, 140, 0.85) 0%, rgba(120, 80, 70, 0.6) 45%, transparent 75%),
      radial-gradient(ellipse 75% 38% at 55% 92%, rgba(220, 80, 60, 0.9) 0%, rgba(200, 120, 60, 0.6) 45%, transparent 80%),
      linear-gradient(180deg, transparent 0%, rgba(60, 40, 50, 0.35) 60%, transparent 100%);
  }
  .brand {
    position: absolute;
    left: 22px;
    top: 18px;
    display: flex;
    align-items: center;
    gap: 10px;
  }
  .brand-dot {
    width: 14px;
    height: 14px;
    border-radius: 50%;
    background: var(--white);
  }
  .brand-name {
    font-family: "PT Sans", sans-serif;
    font-weight: 700;
    font-size: 32px;
    line-height: 1;
    color: var(--white);
  }
  .headline {
    position: absolute;
    left: 19px;
    top: 90px;
    font-family: "Cinzel", serif;
    font-weight: 600;
    font-size: 33px;
    line-height: 40px;
    color: var(--white);
  }
  .occasions {
    position: absolute;
    left: 21px;
    top: 182px;
    font-family: "PT Sans", sans-serif;
    font-weight: 700;
    font-size: 18px;
    line-height: 27px;
    color: var(--white);
  }
  .occasions .divider { padding: 0 8px; }
  .cta {
    position: absolute;
    left: 22px;
    top: 262px;
    width: 158px;
    height: 43px;
    border-radius: 4px;
    border: 1px solid var(--button-edge);
    background: linear-gradient(180deg, var(--button-top) 0%, var(--button-bottom) 100%);
    font-family: "PT Sans", sans-serif;
    font-weight: 700;
    font-size: 20px;
    color: var(--white);
    display: flex;
    align-items: center;
    justify-content: center;
    text-decoration: none;
  }
</style>
</head>
<body>
  <section class="banner">
    <div class="hero-photo" role="img" aria-label="Smiling woman holding a bouquet of colourful roses with butterflies around her"></div>
    <div class="brand">
      <span class="brand-dot"></span>
      <span class="brand-name">CIRANDELLA</span>
    </div>
    <h1 class="headline">Momentos<br>Románticos</h1>
    <p class="occasions">Birthday<span class="divider">I</span>Special Date<br>Anniversary &amp; more...</p>
    <a class="cta" href="http://www.cirandella-example.com.mx">Celebrate now</a>
  </section>
</body>
</html>
```